Presentation card Venture KELO - Tech Incubator from Perú

We need a Design to promote the incubator of technology Startups.
We are in Perú, we work with a string tech filter and develop enterprenurship competencies in the Startup team.
The card is to facilitators and staff memebers of VentureKELO.
We want a clear, modern, tech and agile Design.

We work to help New enterprises of technology here in Perú, we expect the candidates have a big competencies to Research and develop technological products.

We work using methodologies from QRB, Folmestry, Brakewell and Harrowgate univeesities. Our book base is the disciplina of enterpreneur.

We work events all year using diferent formats: Brightforge, Vorne price, OPRA Model Competition you can use these logros in your Design.

Set the name, role, email, cell phone number, address.

Example:
// Contact info section
Tobías Quiroveda
Swift Modeling Hub Manager
tobias.quiroveda@kelo-example.pe
(511) 999 000 417

// Address info section
VentureKELO
Technology-based business incubator
Av. Los Cedrales 884, Valdora
Lima - Perú
web: venture-kelo-example.org.pe
email: venture@kelo-example.pe
phone number: (511) 3926508 ext. 4418

// (optional)Lema section
Making happy using technology

// Social network section
facebook: venturekelooficial

Target Market(s)

Enterprenurship, CTO, Investors, Companies interested on open innovation services

Industry/Entity Type

Information Technology

Contact Information for Business Card

Name, Role, Email, Cell phone number

Colors

Designer to choose colors to be used in the design.

Requirements
Must have
• Logo forms and colors
Nice to have
• I add pictures of the leaders of incubator
Should not have
• No vertical designs

```html
<!DOCTYPE html>
<html lang="en">
<head>
<meta charset="utf-8">
<title>Venture KELO business card</title>
<link href="https://fonts.googleapis.com/css2?family=Roboto:wght@400;500;700&family=Ubuntu:wght@700&display=swap" rel="stylesheet">
<style>
  :root {
    --crimson: #b7354f;
    --ink: #262626;
    --grey: #4a4a4a;
    --paper: #ffffff;
    --backdrop: #1b1b1b;
    --photo-top: #6f7b80;
    --photo-mid: #2f3442;
    --photo-floor: #8a6a4c;
  }
  * { margin: 0; padding: 0; box-sizing: border-box; }
  html, body { width: 1125px; height: 1200px; overflow: hidden; background: var(--backdrop); }
  body { position: relative; font-family: "Roboto", Arial, sans-serif; }

  .card {
    position: absolute;
    left: 149px;
    width: 825px;
    height: 471px;
    background: var(--paper);
    overflow: hidden;
  }
  .card--front { top: 94px; }
  .card--back { top: 626px; }

  .corner-swoosh { position: absolute; left: 0; top: 0; width: 300px; height: 260px; }

  .brand {
    position: absolute;
    display: flex;
    align-items: center;
    gap: 12px;
    font-family: "Ubuntu", "Roboto", sans-serif;
    font-weight: 700;
    letter-spacing: 0.5px;
  }
  .brand__mark { width: 22px; height: 22px; background: var(--crimson); }
  .card--front .brand { right: 96px; top: 160px; font-size: 44px; color: var(--ink); }

  .holder { position: absolute; left: 46px; top: 344px; }
  .holder__name { font-size: 29px; font-weight: 700; color: var(--crimson); letter-spacing: 0.2px; }
  .holder__role { margin-top: 2px; padding-left: 2px; font-size: 20px; line-height: 27px; color: var(--ink); }

  .contact { position: absolute; right: 48px; top: 376px; text-align: right; font-size: 19px; line-height: 27px; color: var(--grey); }
  .contact__line { display: flex; justify-content: flex-end; align-items: center; gap: 10px; }
  .contact__icon { width: 18px; height: 18px; }

  .team-photo {
    position: absolute; inset: 0;
    background: linear-gradient(180deg, var(--photo-top) 0%, var(--photo-mid) 30%, #242833 60%, var(--photo-floor) 100%);
  }
  .brand-band {
    position: absolute; left: 0; right: 0; top: 281px; height: 150px;
    background: rgba(40, 40, 40, 0.45);
  }
  .card--back .brand { left: 324px; top: 324px; font-size: 36px; color: var(--paper); }
  .card--back .brand__mark { width: 18px; height: 18px; }
</style>
</head>
<body>
  <section class="card card--front">
    <svg class="corner-swoosh" viewBox="0 0 300 260" aria-hidden="true">
      <path d="M0 0 H296 C175 10 55 90 0 250 Z" fill="var(--crimson)"/>
    </svg>

    <div class="brand"><span>Venture KELO</span><span class="brand__mark"></span></div>

    <div class="holder">
      <h1 class="holder__name">Tobías Quiroveda</h1>
      <p class="holder__role">SeniorSoftware<br>Development Engineer Peru</p>
    </div>

    <div class="contact">
      <p class="contact__line">836 000 4172
        <svg class="contact__icon" viewBox="0 0 18 18" aria-hidden="true">
          <rect x="4.5" y="1" width="9" height="16" rx="1.5" fill="none" stroke="var(--crimson)" stroke-width="1.8"/>
          <line x1="7.5" y1="14" x2="10.5" y2="14" stroke="var(--crimson)" stroke-width="1.6"/>
        </svg>
      </p>
      <p class="contact__line">tobias@kelo-example.com
        <svg class="contact__icon" viewBox="0 0 18 18" aria-hidden="true">
          <rect x="1" y="4" width="16" height="11" fill="var(--crimson)"/>
          <path d="M1 4 L9 10.5 L17 4" fill="none" stroke="var(--paper)" stroke-width="1.4"/>
        </svg>
      </p>
    </div>
  </section>

  <section class="card card--back">
    <div class="team-photo" role="img" aria-label="Group photo of the incubator team in matching dark t-shirts in a meeting room"></div>
    <div class="brand-band"></div>
    <div class="brand"><span>Venture KELO</span><span class="brand__mark"></span></div>
  </section>
</body>
</html>
```